Business Card Design (NEW FILES)

ATTENTION: New vector files are available. Please update your design to reflect/use the new (better resolution) logo images.

Seeking a unique and professional business card design for a commercial drone photography/videography business. The layout should feature
the logo (attached) and include the following information:
978-512-6037
www.skyvantmedia.com
ORD Certified Remote Pilot

```html
<!DOCTYPE html>
<html lang="en">
<head>
<meta charset="utf-8">
<title>Skyvant Media Business Card</title>
<link rel="stylesheet" href="https://fonts.googleapis.com/css2?family=Open+Sans:wght@400;600;700&display=swap">
<style>
  :root {
    --stage: #232323;
    --navy: #1b1c4b;
    --orange: #e8894c;
    --white: #ffffff;
    --paper: #f4f4f4;
  }
  * { box-sizing: border-box; margin: 0; padding: 0; }
  html, body { width: 1200px; height: 780px; overflow: hidden; }
  body {
    background: var(--stage);
    font-family: "Open Sans", sans-serif;
    position: relative;
  }
  .card {
    position: absolute;
    top: 236px;
    width: 540px;
    height: 309px;
    border-radius: 16px;
    overflow: hidden;
  }
  .card--front { left: 40px; background: var(--white); }
  .card--back { left: 620px; background: var(--paper); }

  .card__waves { position: absolute; inset: 0; width: 540px; height: 309px; }

  .brand {
    position: absolute;
    display: flex;
    align-items: center;
    color: var(--navy);
    font-weight: 600;
    white-space: nowrap;
  }
  .brand__dot {
    border-radius: 50%;
    background: var(--orange);
    flex: none;
  }
  .card--front .brand { left: 38px; top: 42px; font-size: 28px; gap: 10px; }
  .card--front .brand__dot { width: 18px; height: 18px; }
  .card--back .brand {
    left: 0; right: 0; top: 0; bottom: 0;
    justify-content: center;
    font-size: 46px; gap: 16px;
  }
  .card--back .brand__dot { width: 28px; height: 28px; }

  .contact {
    position: absolute;
    right: 30px;
    top: 162px;
    text-align: right;
    color: var(--white);
  }
  .contact__name { font-size: 28px; font-weight: 700; line-height: 32px; }
  .contact__first { color: var(--orange); }
  .contact__role { font-size: 15px; line-height: 20px; }
  .contact__credentials { margin-top: 6px; font-size: 14px; line-height: 19px; }
  .contact__line {
    display: flex; align-items: center; justify-content: flex-end; gap: 8px;
    font-size: 14px; line-height: 20px;
  }
  .contact__icon { width: 13px; height: 13px; flex: none; }
</style>
</head>
<body>

  <section class="card card--front" aria-label="Business card front">
    <svg class="card__waves" viewBox="0 0 540 309" aria-hidden="true">
      <path fill="var(--navy)" d="M0,120 C80,160 170,168 250,162 C370,152 462,94 540,30 L540,309 L0,309 Z"/>
      <path fill="var(--white)" d="M0,140 C80,174 170,180 250,173 C370,162 466,104 540,44 L540,309 L0,309 Z"/>
      <path fill="var(--orange)" d="M0,146 C80,180 170,186 250,179 C370,168 468,110 540,50 L540,309 L0,309 Z"/>
      <path fill="var(--white)" d="M0,162 C80,194 170,199 250,192 C370,182 470,124 540,66 L540,309 L0,309 Z"/>
      <path fill="var(--navy)" d="M0,168 C80,200 170,205 250,198 C370,188 470,130 540,72 L540,309 L0,309 Z"/>
    </svg>

    <div class="brand">
      <span class="brand__dot"></span>
      <span class="brand__name">Skyvant Media</span>
    </div>

    <div class="contact">
      <p class="contact__name"><span class="contact__first">Mark</span> Doyle</p>
      <p class="contact__role">Owner</p>
      <p class="contact__credentials">ORD Certified Remote Pilot<br>Fully Insured</p>
      <p class="contact__line">
        978-512-6037
        <svg class="contact__icon" viewBox="0 0 24 24" aria-hidden="true">
          <path fill="var(--orange)" d="M6.6 10.8a15.1 15.1 0 0 0 6.6 6.6l2.2-2.2a1 1 0 0 1 1-.25 11.4 11.4 0 0 0 3.6.57 1 1 0 0 1 1 1V20a1 1 0 0 1-1 1A17 17 0 0 1 3 4a1 1 0 0 1 1-1h3.5a1 1 0 0 1 1 1c0 1.25.2 2.45.57 3.57a1 1 0 0 1-.25 1z"/>
        </svg>
      </p>
      <p class="contact__line">
        www.skyvantmedia.com
        <svg class="contact__icon" viewBox="0 0 24 24" aria-hidden="true">
          <circle cx="12" cy="12" r="10" fill="none" stroke="var(--orange)" stroke-width="2.4"/>
          <path fill="none" stroke="var(--orange)" stroke-width="2" d="M2 12h20M12 2c3 3 3 17 0 20M12 2c-3 3-3 17 0 20"/>
        </svg>
      </p>
    </div>
  </section>

  <section class="card card--back" aria-label="Business card back">
    <div class="brand">
      <span class="brand__dot"></span>
      <span class="brand__name">Skyvant Media</span>
    </div>
  </section>

</body>
</html>
```